Harbin waste and recycling needs a thank you for business card

We need to design a thank you card for our customers who purchase with us. I like black gloss front and back with thankyou on the front. Or white gloss front back.
The inside should be white and maybe our logo on the bottom right hand side (as you open it up). Maybe put some more pictures on it.

On the inside of the card write -
Congratulations on your recent purchase.
Customers like YOU are the foundation of our business.
We appreciate having YOU as a customer and we look forward to providing you with the best possible service into the future.

PS as an added value if you refer any purchasing clients to Harbin YOU will receive one years free document destruction to the value of $204 or $164 towards a waste and recycling credit. Prices include GST.

Warm Regards,

Dorian Palkett, Business Owner.

Target Market(s)

Business customers within Australia

Industry/Entity Type

Recycling

Colors

Designer to choose colors to be used in the design.

Requirements
Must have
• 'thank you' on the front

'Congratulations on your recent purchase..........' exact text as in project overview. This is to appear on the inside page.

Our logo to be small on the bottom of the inside somewhere
Nice to have
• some more of our pictures

```html
<!DOCTYPE html>
<html lang="en">
<head>
<meta charset="utf-8">
<title>Harbin Waste &amp; Recycling – Thank You Card</title>
<link href="https://fonts.googleapis.com/css2?family=Stardos+Stencil:wght@700&family=Mulish:ital,wght@1,400;1,600&display=swap" rel="stylesheet">
<style>
  :root {
    --teal: #0f777c;
    --teal-soft: #3f9599;
    --ink: #4a4a4a;
    --paper: #ffffff;
    --frame: #8a8a8a;
    --brand: #1f1f1f;
  }
  * { box-sizing: border-box; margin: 0; padding: 0; }
  html, body { width: 1200px; height: 480px; overflow: hidden; background: var(--paper); }
  .canvas { position: relative; width: 1200px; height: 480px; }

  .card { position: absolute; top: 59px; width: 514px; height: 338px; }

  .card-front { left: 58px; background: var(--teal); overflow: hidden; }
  .front-emblem {
    position: absolute; left: 137px; top: 36px; width: 240px; height: 266px;
    border-radius: 50%;
    background: radial-gradient(circle, rgba(255,255,255,0.16) 0%, rgba(255,255,255,0.08) 55%, rgba(255,255,255,0) 72%);
  }
  .front-title {
    position: absolute; left: 0; right: 0; top: 196px;
    text-align: center; color: var(--paper);
    font-family: "Stardos Stencil", "Arial Black", sans-serif; font-weight: 700;
    font-size: 56px; letter-spacing: 1px; line-height: 1;
  }

  .card-inside { left: 612px; background: var(--paper); border: 1.5px solid var(--frame); }
  .message {
    position: absolute; left: 0; right: 0; top: 40px; text-align: center;
    font-family: "Mulish", "Trebuchet MS", sans-serif; font-style: italic;
    color: var(--teal); font-size: 13.5px; line-height: 17px;
  }
  .message p + p { margin-top: 11px; }
  .postscript, .signoff, .signature {
    position: absolute; left: 70px;
    font-family: "Mulish", "Trebuchet MS", sans-serif; font-style: italic;
    color: var(--ink); font-size: 10.6px; line-height: 15.5px;
  }
  .postscript { top: 162px; width: 380px; }
  .postscript .ps-mark { font-size: 14px; }
  .signoff { top: 232px; }
  .signature { top: 286px; }

  .brand {
    position: absolute; left: 262px; top: 262px;
    display: flex; align-items: center; gap: 10px;
  }
  .brand-square { width: 22px; height: 22px; background: var(--teal); }
  .brand-name {
    font-family: "Mulish", "Trebuchet MS", sans-serif; font-style: italic; font-weight: 600;
    font-size: 17px; color: var(--brand); letter-spacing: 0.3px;
  }
</style>
</head>
<body>
<main class="canvas">
  <section class="card card-front" aria-label="Card front">
    <div class="front-emblem" role="img" aria-label="Faint recycling arrows symbol behind the title"></div>
    <h1 class="front-title">THANK YOU</h1>
  </section>

  <section class="card card-inside" aria-label="Card inside">
    <div class="message">
      <p>Congratulations on your recent purchase.</p>
      <p>Customers like YOU are the foundation of our business.</p>
      <p>We appreciate having YOU as a customer and we look<br>forward to providing you with the best possible service<br>into the future.</p>
    </div>
    <p class="postscript"><span class="ps-mark">PS</span> as an added value if you refer any purchasing clients to Harbin YOU will receive one years free document destruction to the value of $204 or $164 towards a waste and recycling credit.<br>Prices include GST.</p>
    <p class="signoff">Warm regards,</p>
    <p class="signature">Dorian Palkett,<br>Business Owner</p>
    <div class="brand">
      <span class="brand-square" aria-hidden="true"></span>
      <span class="brand-name">Harbin Waste &amp; Recycling</span>
    </div>
  </section>
</main>
</body>
</html>
```